Kelbrook Training Australia - Course Brochure Design

Kelbrook Training Australia is a Private Register Training Organisation that delivery accredited training courses to students. These courses are delivery via face to face training and distance education (e.g. elearning).

We are looking to get a template designed via adobe in design that we can use for each of our courses and list the information relevant for each one.

It will need to be around 3 - 4 pages long to be able to fit the information required into the brochure, i have attached some example of other providers course information sheets.

From the examples you'll be able to see that most of the information will remained the same until it gets to the course structure.

I would like it to be kept within our current theme, we are in the middle of upgrading our new website and look (www.kelbrook.com.au/drupal).

I look forward to see what you all come back with.

Reason: Hi everyone, Thanks for submitting your design, I have extended the deadline due to not many designs have been submitted. I will be review and providing feedback on the designed submitted this week and will provide some more information based off the work and direction of the designs submitted. Thanks, Ralph.

Target Market(s)

our target market is business and individuals who would like to undergo training course. This brochure needs to display the require information.

Industry/Entity Type

Education

Requirements
Must have
• The brochure must have a front page with a design to list our company logo and information and the course title.

A call to action must be on every page, e.g. footer to enrol now call kelbok on 1800 392 508 or visit www.kelbrook.com.au

Nice to have
• Some picture to fill the pages would add a nice look

```html
<!DOCTYPE html>
<html lang="en">
<head>
<meta charset="utf-8">
<title>Kelbrook Training Australia – Course Brochure Spread</title>
<link rel="stylesheet" href="https://fonts.googleapis.com/css2?family=Open+Sans:wght@400;600;700&display=swap">
<style>
  :root {
    --backdrop: #9a9ea3;
    --paper: #ffffff;
    --brand-red: #8c1b14;
    --accent-red: #a3281f;
    --body-grey: #6b6b6b;
    --soft-grey: #eeeeee;
    --rule-grey: #d9d9d9;
    --table-head: #e4e4e4;
  }
  * { box-sizing: border-box; margin: 0; padding: 0; }
  html, body { width: 1200px; height: 900px; overflow: hidden; }
  body {
    background: var(--backdrop);
    font-family: "Open Sans", Arial, sans-serif;
    color: var(--body-grey);
    position: relative;
  }
  .page {
    position: absolute;
    top: 44px;
    width: 572px;
    height: 820px;
    background: var(--paper);
    overflow: hidden;
    box-shadow: 0 2px 8px rgba(0,0,0,0.25);
  }
  .page--left { left: 20px; }
  .page--right { left: 604px; }

  /* ---------- left page ---------- */
  .header-strip {
    position: absolute; top: 0; left: 0; width: 572px; height: 76px;
    background: linear-gradient(90deg, #e2e2e2 0%, #f4f4f4 60%, #fafafa 100%);
  }
  .header-strip__people {
    position: absolute; top: 0; left: 0; width: 200px; height: 76px;
    background: linear-gradient(90deg, #6d5a4f 0%, #b89a86 45%, #d8cfc8 100%);
  }
  .title-band {
    position: absolute; top: 80px; left: 36px; width: 496px; height: 36px;
    background: var(--brand-red);
    color: #fff; font-size: 17px; font-weight: 700;
    line-height: 36px; padding-left: 30px;
  }
  .intro {
    position: absolute; top: 134px; left: 36px; width: 500px;
    color: var(--accent-red); font-size: 16.5px; line-height: 24px;
  }
  .section-label {
    font-size: 10px; font-weight: 700; color: var(--accent-red);
    text-transform: uppercase; letter-spacing: 0.2px;
  }
  .left-intro-label { position: absolute; top: 230px; left: 36px; }
  .body-copy { font-size: 9.5px; line-height: 15px; color: var(--body-grey); }
  .left-column {
    position: absolute; top: 252px; left: 36px; width: 214px; text-align: justify;
  }
  .left-column p + p { margin-top: 8px; }
  .feature-photo {
    position: absolute; top: 228px; left: 262px; width: 282px; height: 282px;
    background: linear-gradient(135deg, #c9c4c0 0%, #a99385 40%, #7d7670 70%, #dcdcdc 100%);
  }
  .info-band {
    position: absolute; top: 572px; left: 0; width: 572px; height: 208px;
    background: var(--soft-grey);
  }
  .info-col { position: absolute; top: 588px; }
  .info-col--one { left: 36px; width: 140px; }
  .info-col--two { left: 192px; width: 168px; }
  .info-col--three { left: 380px; width: 160px; }
  .info-col .section-label { margin-bottom: 6px; }
  .info-col .body-copy { font-size: 9px; line-height: 14px; }
  .bullet-list { list-style: none; margin-top: 6px; }
  .bullet-list li {
    position: relative; padding-left: 14px; margin-bottom: 6px;
    font-size: 9px; line-height: 14px;
  }
  .bullet-list li::before {
    content: ""; position: absolute; left: 0; top: 4px;
    width: 6px; height: 6px; background: var(--accent-red);
  }
  .page-footer {
    position: absolute; bottom: 0; left: 0; width: 572px; height: 40px;
    font-size: 10px; line-height: 40px; text-align: center; color: #8a8a8a;
  }
  .page-footer strong { color: #555; font-weight: 700; }
  .footer-tab {
    position: absolute; bottom: 0; width: 40px; height: 40px; background: var(--brand-red);
  }
  .page--left .footer-tab { left: 0; }
  .page--right .footer-tab { right: 0; }

  /* ---------- right page ---------- */
  .running-head {
    position: absolute; top: 10px; right: 20px;
    font-size: 10px; color: #777; display: flex; align-items: center; gap: 8px;
  }
  .running-head::after {
    content: ""; width: 4px; height: 14px; background: var(--brand-red);
  }
  .team-photo {
    position: absolute; top: 52px; left: 0; width: 572px; height: 214px;
    background: linear-gradient(90deg, #7a1712 0%, #a8382e 30%, #c8b2a4 55%, #9c8878 75%, #d2d2d2 100%);
  }
  .structure-label { position: absolute; left: 36px; }
  .structure-label--units { top: 284px; }
  .structure-label--table { top: 546px; }
  .unit-grid {
    position: absolute; top: 310px; left: 36px; width: 510px;
    display: grid; grid-template-columns: repeat(3, 1fr);
    column-gap: 20px; row-gap: 14px;
  }
  .unit { position: relative; padding-left: 14px; }
  .unit::before {
    content: ""; position: absolute; left: 0; top: 4px;
    width: 6px; height: 6px; background: var(--accent-red);
  }
  .unit__title { font-size: 9px; font-weight: 700; color: var(--accent-red); line-height: 14px; }
  .unit__text { font-size: 8.5px; line-height: 13px; color: var(--body-grey); }
  .course-table {
    position: absolute; top: 570px; left: 36px; width: 510px;
    border-collapse: collapse; font-size: 8.5px; line-height: 13px;
  }
  .course-table th {
    background: var(--table-head); text-align: left;
    font-size: 9px; font-weight: 600; color: #666; padding: 8px 10px;
    text-transform: uppercase;
  }
  .course-table td {
    padding: 7px 10px; vertical-align: top; border-bottom: 1px solid var(--rule-grey);
  }
  .course-table .col-code { width: 80px; }
  .course-table .col-unit { width: 140px; }
</style>
</head>
<body>

<section class="page page--left">
  <div class="header-strip">
    <div class="header-strip__people" role="img" aria-label="Photo of smiling students in a training session"></div>
  </div>
  <h1 class="title-band">Quidit endes esenis de explita eum</h1>
  <p class="intro">Musapic atempor andebit perum, sit, velitas piendipsae nemquam volupta doluptasped quiatur aut ut aceptasimos ut lacipiendis duntiat uribeatio. Et ma pliquas et et lacepe num exped.</p>

  <h2 class="section-label left-intro-label">Musapic atempor andebit perum</h2>
  <div class="left-column body-copy">
    <p>Velles pienimpel nemquam volupta dolupta quiatur aut ut aceptatios ut lacipiendis duntiat utem ut et moditem, ipsam quo earum estrum officabo. Ut et, nobis eatus dolorem eum quam vel ipsam, officid que nimus estrum quatur, comnimo magnat apienda sit ut lam nostrum aut harum.</p>
    <p>Quis re maximpe latemnum rem quatus aut ipsam facea nobis alis erferum quiatem.</p>
  </div>
  <div class="feature-photo" role="img" aria-label="Photo of a smiling student using a tablet with classmates behind"></div>

  <div class="info-band"></div>
  <div class="info-col info-col--one">
    <h3 class="section-label">Dicat et, solum cus</h3>
    <p class="body-copy">Excera is nullec natis sitatur adisque erferi blaten endus que non tem. Optiunt, omnitiis simolent ectaqua boreh dolorem quisquid sita voluptatur molupitat faccae nam haris estorum andebis acernat.</p>
  </div>
  <div class="info-col info-col--two">
    <h3 class="section-label">Eostrum andebis acernat</h3>
    <p class="body-copy">Excera is nullec natis sitatur adisque erferi enduis que non tem. Optiunt, omnitiis.</p>
    <ul class="bullet-list body-copy">
      <li>Imolant ectaqua blaten dolorem</li>
      <li>Faccae nam haris quidenditas</li>
      <li>Ducimporo molestiae volup</li>
      <li>Erepedi atem velorr aut fugia</li>
    </ul>
  </div>
  <div class="info-col info-col--three">
    <ul class="bullet-list body-copy">
      <li>Rum, con nos et eos eos ipsae quost</li>
      <li>Nictam platio eicaem qui los, ut et voluptatem</li>
      <li>adionemos estrum quiatus que sint pelleus</li>
      <li>imolec aut maximintem ex fugit explit sunt</li>
      <li>sol moditaque eos conem</li>
    </ul>
  </div>

  <footer class="page-footer">To enrol now, call Kelbrook on <strong>1800 392 508</strong> or visit <strong>www.kelbrook.com.au</strong></footer>
  <div class="footer-tab"></div>
</section>

<section class="page page--right">
  <div class="running-head">Quidit endes esenis de explita eum</div>
  <div class="team-photo" role="img" aria-label="Photo of a smiling group of business professionals with a red tint on the left"></div>

  <h2 class="section-label structure-label structure-label--units">Nam rerem es doloreptios dunt, si bere volupic iditatq ussequis</h2>
  <div class="unit-grid">
    <div class="unit"><p class="unit__title">Volor aut molor molorro eum</p><p class="unit__text">Quatum quas volupit omnis dit laendit aut utem, aliquatur ant volupta dolor.</p></div>
    <div class="unit"><p class="unit__title">Molor molorro eum</p><p class="unit__text">Quatum quas volupit omnis dit laendit aut utem, aliquatur ant volupta dolor.</p></div>
    <div class="unit"><p class="unit__title">Aut molor molorro eum</p><p class="unit__text">Quatum quas volupit omnis dit laendit aut utem, aliquatur ant volupta dolor.</p></div>
    <div class="unit"><p class="unit__title">Dentatur sitint omnitiqu</p><p class="unit__text">Rempore ciendip sinhentur alit faceperum aut que dolupta velendis quos nimint.</p></div>
    <div class="unit"><p class="unit__title">Iutur sitint omnitiqu</p><p class="unit__text">Rempore ciendip sinhentur alit faceperum aut que dolupta velendis quos nimint.</p></div>
    <div class="unit"><p class="unit__title">Rnatur sitint omnitiqu</p><p class="unit__text">Rempore ciendip sinhentur alit faceperum aut que dolupta velendis quos nimint.</p></div>
    <div class="unit"><p class="unit__title">con temporum necaper</p><p class="unit__text">Orehente octoreperf et quiant estrum eume dolorat alitia dolut facia test mint.</p></div>
    <div class="unit"><p class="unit__title">Tempornm necaper</p><p class="unit__text">Orehente octoreperf et quiant estrum eume dolorat alitia dolut facia test mint.</p></div>
    <div class="unit"><p class="unit__title">Porrum necaper</p><p class="unit__text">Orehente octoreperf et quiant estrum eume dolorat alitia dolut facia test mint.</p></div>
  </div>

  <h2 class="section-label structure-label structure-label--table">Nam rerem es doloreptios dunt, si bere volupic iditatq ussequis</h2>
  <table class="course-table">
    <thead>
      <tr><th class="col-code">Ria sindit</th><th class="col-unit">Ut labor alis</th><th>Mod quam fuga. Illibusam ipsapid</th></tr>
    </thead>
    <tbody>
      <tr><td></td><td>Ci ki aut ut demnique alisitatius eto tempor</td><td>Item quo moluptatius eic dolupta tiberite nobis modi nus ut quiatem as quas et ea aut in consed que pratusam quiate</td></tr>
      <tr><td></td><td>poruptasint ipsam</td><td>omnis modi omnia volupti que vellan sim cus cuptatem volorem et magnim enis nonse que vel mo maximus</td></tr>
      <tr><td></td><td>maximus et odigentas, Et am nimus</td><td>iunto imo et qui repro maximporum quo eaquis ditatus sim, Non quo quid eum doluptae ectur rerum</td></tr>
      <tr><td></td><td>seliquamus ras expel</td><td>genimus as ipsam qui pro etur minis rentectiae dolor aut</td></tr>
    </tbody>
  </table>

  <footer class="page-footer">To enrol now, call Kelbrook on <strong>1800 392 508</strong> or visit <strong>www.kelbrook.com.au</strong></footer>
  <div class="footer-tab"></div>
</section>

</body>
</html>
```